Harbourline Advisory Group - Business card design needed

I wish to get business cards designed so that it follows my website design ... http://www.harbourline-advisory.org
I need logos for KELMOR 4 and Quarvex Channel Member for myself which I have uploaded the files.
I wish my qualifications PhD PMP FAICD to be smaller print than my name.
Regards
Leonard
Industry/Entity Type
Business
Contact Information for Business Card
Harbourline Advisory Group
Dr Leonard Pryce PhD PMP FAICD
Director
PO Box 318 Cremorvale NSW 2093 AUSTRALIA
T:+61 2 9356 4702 M:+61 423 870515 F: +61 2 9318 6200
Email: leonard.pryce@harbourline-advisory.org
Website: http://www.harbourline-advisory.org
Look and feel
Each slider illustrates characteristics of the customer's brand and the style your logo design should communicate.

```html
<!DOCTYPE html>
<html lang="en">
<head>
<meta charset="utf-8">
<title>Harbourline Advisory Group – Business Card</title>
<link rel="stylesheet" href="https://fonts.googleapis.com/css2?family=Lato:ital,wght@0,400;0,700;1,400&display=swap">
<style>
  :root {
    --stage: #e4e6ea;
    --card: #ffffff;
    --band-dark: #363b42;
    --band-light: #4f5a66;
    --title: #ffffff;
    --ink: #2a2d31;
    --muted: #5c5f64;
    --badge-light: #ffffff;
    --badge-blue: #0d96d6;
  }
  html, body {
    margin: 0;
    width: 1200px;
    height: 944px;
    overflow: hidden;
    background: var(--stage);
    font-family: "Lato", Arial, sans-serif;
  }
  .business-card {
    position: absolute;
    left: 173px;
    top: 215px;
    width: 841px;
    height: 524px;
    background: var(--card);
    box-shadow: 0 4px 14px rgba(0,0,0,0.18);
    overflow: hidden;
  }
  .card-header {
    position: absolute;
    left: 0; top: 0;
    width: 100%;
    height: 215px;
    background: radial-gradient(ellipse at 50% 45%, var(--band-light) 0%, var(--band-dark) 75%);
  }
  .company-name {
    position: absolute;
    left: 0; right: 0;
    top: 37px;
    margin: 0;
    text-align: center;
    color: var(--title);
    font-weight: 700;
    font-size: 44px;
    line-height: 48px;
    letter-spacing: 0.2px;
  }
  .badge {
    position: absolute;
  }
  .badge--certification {
    left: 154px; top: 113px;
    width: 244px; height: 87px;
    background: var(--badge-light);
  }
  .badge--partner {
    left: 466px; top: 120px;
    width: 220px; height: 78px;
    background: var(--badge-blue);
  }
  .line {
    position: absolute;
    margin: 0;
    line-height: 1.1;
    white-space: nowrap;
  }
  .person-name { left: 31px; top: 252px; font-size: 31px; color: var(--muted); }
  .credentials { left: 31px; top: 300px; font-size: 23px; font-style: italic; color: var(--ink); }
  .role { left: 31px; top: 331px; font-size: 25px; color: var(--ink); }
  .address { left: 31px; font-size: 24px; color: var(--muted); }
  .address--one { top: 391px; }
  .address--two { top: 437px; }

  .contact { left: 409px; font-size: 25px; color: var(--ink); }
  .contact .label { display: inline-block; width: 28px; color: var(--muted); }
  .contact .sep { display: inline-block; width: 37px; color: var(--muted); }
  .contact--t { top: 255px; }
  .contact--m { top: 287px; }
  .contact--f { top: 319px; }
  .contact--e { top: 369px; }
  .contact--e2 { top: 401px; left: 474px; }
  .contact--w { top: 435px; }
</style>
</head>
<body>
  <article class="business-card">
    <header class="card-header">
      <h1 class="company-name">Harbourline Advisory Group</h1>
      <div class="badge badge--certification" role="img" aria-label="KELMOR 4 certification badge"></div>
      <div class="badge badge--partner" role="img" aria-label="Quarvex Channel Member badge"></div>
    </header>

    <p class="line person-name">Dr Leonard Pryce</p>
    <p class="line credentials">PhD PMP FAICD</p>
    <p class="line role">Director</p>
    <p class="line address address--one">PO Box : 318,Cremorvale</p>
    <p class="line address address--two">NSW 2093, AUSTRALIA</p>

    <p class="line contact contact--t"><span class="label">T</span><span class="sep">:</span>+61 2 9356 4702</p>
    <p class="line contact contact--m"><span class="label">M</span><span class="sep">:</span>+61 423 870515</p>
    <p class="line contact contact--f"><span class="label">F</span><span class="sep">:</span>+61 2 9318 6200</p>
    <p class="line contact contact--e"><span class="label">E</span><span class="sep">:</span>leonard.pryce@</p>
    <p class="line contact contact--e2">harbourline-advisory.org</p>
    <p class="line contact contact--w"><span class="label">W</span><span class="sep">:</span>www.harbourline-advisory.org</p>
  </article>
</body>
</html>
```